Flyer needed to promote gutter clearance service for established gardening company

We need a bright and engaging flyer to be designed to advertise our gutter clearance service.
Whilst we are a gardening company that normally does more horticultural work, during the winter we offer other services such as gutter clearance where we remove the debris from gutters and thereby reducing the risk of clogs, leakage, breakage and potential structural damage to the property.

Full details of our service, together with our overall brand and colours can be seen on www.hartleyoutdoorcare.co.uk/gutters.

We would like you to use the page on the website as a basis to create the flyer and so please feel free to use as much or as little of the wording contained within the webpage on the flyer drawing particular attention to "Prices starting at just £60 for an average 3 bed house". I will upload pictures but please feel free to use other graphics and fonts to make it stand out.

The contact details which should be included within the flyer are as follows:

Hartley Outdoor Care Ltd
Kestrel Trade Park
Whitlow Moor Ind Estate
Swindon
SN3 7QL

Tel: 01793 418203
www.hartleyoutdoorcare.co.uk
mark@hartleyoutdoorcare.co.uk

The flyers will eventually be printed out in A5 (210mm x 148mm) using Printaloft and so needs to be in that size and suitable file for upload.

I have only put this as a 2 day project as its really urgent and I'm hoping we get some great designs in that time.

Target Market(s)

Homeowners between 25 - 65+

Industry/Entity Type

Home Improvement

Font styles to use
Serif
Sans Serif
Decorative
Script

Colors
6b449b
9bcb3c

Requirements
Must have
• Our colours are purple and green as seen on our website www.hartleyoutdoorcare.co.uk/gutters. Please use those colours.
• The flyer should draw attention to the following facts:
• We are Hartley Outdoor Care Ltd (see attached logo)
• We are offering a Gutter Clearance Service in Swindon
• Prices start at just £60 for the average 3 bed house.
• We are fully insured.
• Our contact details must be included (as in the product description above)
• I have attached pictures but feel free to add other graphics or use fonts to make the flyer more engaging and interesting.
• Additional wording may be taken from the website at the address shown above. You can use as much or as little wording as you like just as long as the message gets across and the flyer contains our contact information and logo and the details shown above.
Nice to have
• I would like a bright and modern design which isn't too busy or cluttered. It should be something that is quick and easy to read.
Should not have
• I don't want it to look too busy or crowded with small type which people just won't read. Whilst I've said you can take whatever wording you want from our website, I'd suggest you don't take it all or too much. I want the main message (as detailed above in 'must haves') to stand out rather than have it contained deep within lots of small type face.

```html
<!DOCTYPE html>
<html lang="en">
<head>
<meta charset="utf-8">
<title>Hartley Outdoor Care – Gutter Clearance Flyer</title>
<link rel="stylesheet" href="https://fonts.googleapis.com/css2?family=Montserrat:wght@500;600;700;800&display=swap">
<style>
  :root {
    --brand-green: #9bcb3c;
    --brand-purple: #6b449b;
    --logo-green: #4f6b2a;
    --ink: #111111;
    --paper: #ffffff;
    --gutter-dark: #3a3f44;
    --garden-green: #7a9a3a;
    --bench-grey: #8d8f8c;
  }
  * { margin: 0; padding: 0; box-sizing: border-box; }
  html, body { width: 1200px; height: 845px; overflow: hidden; background: var(--paper); }
  .flyer {
    position: relative;
    width: 1200px;
    height: 845px;
    font-family: "Montserrat", Arial, sans-serif;
    background: var(--paper);
    overflow: hidden;
  }
  .photo-gutter {
    position: absolute;
    left: 0; top: 0;
    width: 1200px; height: 358px;
    background:
      radial-gradient(ellipse at 78% 30%, rgba(122,154,58,0.85) 0%, rgba(122,154,58,0) 55%),
      radial-gradient(ellipse at 30% 55%, rgba(217,166,58,0.75) 0%, rgba(217,166,58,0) 45%),
      linear-gradient(160deg, var(--gutter-dark) 0%, #55605a 45%, var(--garden-green) 100%);
  }
  .headline-box {
    position: absolute;
    left: 400px; top: 132px;
    width: 397px; height: 112px;
    background: var(--brand-green);
    display: flex;
    align-items: center;
    justify-content: center;
  }
  .headline {
    color: var(--paper);
    font-weight: 700;
    font-size: 31px;
    line-height: 1.22;
    text-align: center;
  }
  .price-badge {
    position: absolute;
    left: 912px; top: 62px;
    width: 230px; height: 230px;
    border-radius: 50%;
    background: var(--brand-purple);
    color: var(--paper);
    display: flex;
    flex-direction: column;
    align-items: center;
    justify-content: center;
    text-align: center;
    padding: 0 26px;
  }
  .price-service { font-weight: 600; font-size: 13px; line-height: 1.3; }
  .price-lead { font-weight: 600; font-size: 16px; margin-top: 6px; }
  .price-amount { font-weight: 800; font-size: 56px; line-height: 1; color: var(--brand-green); }
  .price-note { font-weight: 500; font-size: 13px; line-height: 1.3; margin-top: 4px; }
  .info-band {
    position: absolute;
    left: 0; top: 358px;
    width: 1200px; height: 110px;
    background: var(--paper);
  }
  .question {
    position: absolute;
    left: 61px; top: 32px;
    font-weight: 700;
    font-size: 21px;
    line-height: 1.3;
    color: var(--ink);
  }
  .web-address {
    position: absolute;
    left: 447px; top: 43px;
    font-weight: 500;
    font-size: 21px;
    color: var(--ink);
  }
  .brand-name {
    position: absolute;
    left: 910px; top: 30px;
    display: flex;
    align-items: center;
    gap: 12px;
  }
  .brand-dot {
    width: 26px; height: 26px;
    border-radius: 50%;
    background: var(--brand-green);
  }
  .brand-text {
    font-weight: 700;
    font-size: 22px;
    line-height: 1.15;
    color: var(--logo-green);
  }
  .photo-pots {
    position: absolute;
    left: 0; top: 468px;
    width: 1200px; height: 377px;
    background:
      radial-gradient(ellipse at 20% 40%, rgba(233,120,170,0.7) 0%, rgba(233,120,170,0) 30%),
      radial-gradient(ellipse at 45% 60%, rgba(201,101,47,0.95) 0%, rgba(201,101,47,0) 40%),
      radial-gradient(ellipse at 82% 62%, rgba(201,101,47,0.9) 0%, rgba(201,101,47,0) 42%),
      radial-gradient(ellipse at 75% 20%, rgba(240,210,60,0.6) 0%, rgba(240,210,60,0) 28%),
      linear-gradient(180deg, var(--bench-grey) 0%, #6f6c66 60%, #4d4a45 100%);
  }
  .contact-bar {
    position: absolute;
    left: 0; top: 771px;
    width: 1200px; height: 74px;
    background: var(--brand-purple);
    color: var(--paper);
    display: flex;
    align-items: center;
    justify-content: space-between;
    padding: 0 61px;
  }
  .insured-tag {
    background: var(--brand-green);
    color: var(--paper);
    font-weight: 700;
    font-size: 18px;
    padding: 9px 18px;
    white-space: nowrap;
  }
  .contact-details {
    font-weight: 500;
    font-size: 14px;
    line-height: 1.45;
    text-align: right;
  }
  .contact-details strong { font-weight: 700; }
</style>
</head>
<body>
  <main class="flyer">
    <div class="photo-gutter" role="img" aria-label="Gloved hands clearing autumn leaves from a grey roof gutter, with a green garden behind"></div>

    <div class="headline-box">
      <p class="headline">A great way to avoid<br>damage to your home</p>
    </div>

    <div class="price-badge">
      <p class="price-service">Gutter clearance in Swindon</p>
      <p class="price-lead">Prices from just</p>
      <p class="price-amount">£60</p>
      <p class="price-note">for an average<br>3 bed house</p>
    </div>

    <section class="info-band">
      <p class="question">When was the last time<br>you cleared your gutters?</p>
      <p class="web-address">www.hartleyoutdoorcare.co.uk</p>
      <div class="brand-name">
        <span class="brand-dot"></span>
        <span class="brand-text">Hartley<br>Outdoor Care</span>
      </div>
    </section>

    <div class="photo-pots" role="img" aria-label="Terracotta flower pots and a window box planted with pink primulas and yellow and purple pansies on a garden bench"></div>

    <footer class="contact-bar">
      <p class="insured-tag">Fully insured</p>
      <p class="contact-details">
        <strong>Hartley Outdoor Care Ltd</strong>, Kestrel Trade Park, Whitlow Moor Ind Estate, Swindon SN3 7QL<br>
        Tel: <strong>01793 418203</strong> &nbsp;·&nbsp; mark@hartleyoutdoorcare.co.uk &nbsp;·&nbsp; www.hartleyoutdoorcare.co.uk
      </p>
    </footer>
  </main>
</body>
</html>
```